Book Cover for Collection of Dark Short Stories

I need a cover design for my book "Amber Hollows." It will be a 5 x 8 paperback roughly 200 pages long. There will be 11 short stories in it of a darker nature. The book is a mixture of science fiction, historical fiction, and just interesting to read stories. The stories focus on individuals or people facing difficult situations such as terrifying end of the world scenarios, mortal danger in wars, as well as crushing debt and a job layoff.
I envision the cover with dark colors (blue/black). One suggestion is to have the silhouette of a man outside sitting on a log or hill with him looking slightly down in contemplation. There are dark clouds covering most of the sky, but the stars and/or moon are trying to shine through in one small area. There's a small amount of hope in the gloom.
I see the mood of the cover as darkly reflective.

I will be happy to look at other suggestions, too.

I will also have some text on the back with a small author photo in the middle. I see the back cover as a continuation of the front cover with dark clouds and again the small amount of light from the moon and stars.
I don't want any violence or death in the cover.
I'll be happy to look at suggestions for the back cover area from the designers.

The title of the book is: AMBER HOLLOWS a subtitle in a smaller font somewhere below should read: A Collection of Short Stories My name should be at the bottom of the cover: Dana Whitcombe

Hey designers, Please find the text for the back cover here: This fascinating collection of short stories is a unique blend of science fiction, action, and historical fiction that will entertain and challenge you. In Amber Hollows’ 11 intriguing stories, we experience one isolated man’s survival as he holds out and awaits the terrifying arrival of otherworldly visitors; firsthand battlefield accounts with some strange occurrences in both WW II and the Revolutionary War; and a tiger hunt in India that goes very wrong. We also see tales of modern woe revolving around some of life’s common miseries, accompanied by brave and unexpected measures to fight against them. In addition, we witness an awkward and dangerous stay in an underground bunker with an unstable host; two astronauts stranded on a lifeless asteroid who only have one old-fashioned form of entertainment; an eerie post-plague world dominated by an unlikely species; and an eccentric astronaut orbiting the Earth who is happiest on his own, except for one furry exception. Dana Whitcombe’s interesting stories travel in different directions, but spring from one deep source: the darker side of the imagination. I also have an author photo that I would like either below the text or in between, whichever looks better. Feel free to crop it without my hands or whatever looks best.

Target Market(s)

Men 18-65, but crossover appeal to women is fine, too.

Font styles to use
Serif

Colors
0255a3
000000
1b1b1b
dcdcdc
fbf289

Requirements
Must have
• AMBER HOLLOWS in some form.
Nice to have
• Some interesting takes on AMBER HOLLOWS and the silhouette of a man sitting and contemplating deep things (like the end of the world).
Should not have
• No violence, sex, death, or anything provocative in the cover. I want to convey a serious, dark contemplative mood with a slight amount of hope.

```html
<!DOCTYPE html>
<html lang="en">
<head>
<meta charset="utf-8">
<title>Amber Hollows – Cover Spread</title>
<link rel="stylesheet" href="https://fonts.googleapis.com/css2?family=Cinzel:wght@400;500&family=Montserrat:wght@300;400;500;700&display=swap">
<style>
  :root {
    --page: #ffffff;
    --night: #03070f;
    --navy: #0a1c38;
    --blue: #0255a3;
    --glow: #2d5f96;
    --ink: #ffffff;
    --soft: #dcdcdc;
    --moon: #c9c9cf;
  }
  * { margin: 0; padding: 0; box-sizing: border-box; }
  html, body {
    width: 960px; height: 1200px; overflow: hidden;
    background: var(--page);
  }
  .spread {
    position: absolute; left: 20px; top: 265px;
    width: 920px; height: 669px;
    overflow: hidden;
    background: var(--night);
    color: var(--ink);
    font-family: "Montserrat", sans-serif;
  }
  .sky {
    position: absolute; inset: 0;
    background:
      radial-gradient(ellipse 40% 45% at 70% 35%, rgba(18,48,92,.7), transparent 70%),
      radial-gradient(ellipse 35% 50% at 20% 40%, rgba(12,34,70,.75), transparent 70%),
      linear-gradient(180deg, #050d1c 0%, #081a33 45%, #02050b 100%);
  }
  .spine {
    position: absolute; left: 418px; top: 0; width: 82px; height: 100%;
    background: linear-gradient(180deg, #0d2545 0%, #0a1d38 50%, #060f1f 100%);
  }
  /* Back cover */
  .back-title {
    position: absolute; left: 0; width: 418px; top: 110px;
    text-align: center; font-weight: 700; font-size: 37px; letter-spacing: -0.5px; line-height: 1;
  }
  .back-subtitle {
    position: absolute; left: 0; width: 418px; top: 160px;
    text-align: center; font-weight: 300; font-size: 15.5px;
  }
  .back-author {
    position: absolute; left: 0; width: 418px; top: 192px;
    text-align: center; font-family: "Cinzel", serif; font-size: 21px; letter-spacing: 0.5px;
  }
  .author-photo {
    position: absolute; left: 44px; top: 250px; width: 114px; height: 160px;
    background: linear-gradient(160deg, #6f7560 0%, #4a4d44 45%, #1e2530 100%);
  }
  .blurb { text-align: justify; font-weight: 500; color: var(--ink); }
  .blurb-side {
    position: absolute; left: 167px; top: 250px; width: 213px;
    font-size: 9.3px; line-height: 14px;
  }
  .blurb-side p + p { margin-top: 14px; }
  .blurb-wide {
    position: absolute; left: 40px; top: 424px; width: 340px;
    font-size: 9.9px; line-height: 15.3px;
  }
  /* Spine */
  .spine-title {
    position: absolute; left: 452px; top: 118px;
    writing-mode: vertical-rl;
    font-weight: 700; font-size: 35px; line-height: 1; letter-spacing: -0.5px;
  }
  .spine-subtitle {
    position: absolute; left: 432px; top: 184px;
    writing-mode: vertical-rl;
    font-weight: 300; font-size: 13px; line-height: 1;
  }
  .spine-author {
    position: absolute; left: 418px; width: 82px; top: 608px;
    text-align: center; font-family: "Cinzel", serif; font-size: 13px; line-height: 16px;
  }
  /* Front cover */
  .moon {
    position: absolute; left: 806px; top: 69px; width: 66px; height: 66px; border-radius: 50%;
    background: radial-gradient(circle at 40% 40%, #e4e4ea 0%, var(--moon) 55%, #8d8f99 100%);
    box-shadow: 0 0 14px rgba(200,210,240,.35);
  }
  .front-title {
    position: absolute; left: 500px; width: 420px; top: 140px;
    text-align: center; font-weight: 700; font-size: 58px; line-height: 74px; letter-spacing: -1px;
  }
  .front-subtitle {
    position: absolute; left: 500px; width: 420px; top: 306px;
    text-align: center; font-weight: 300; font-size: 20px;
  }
  .front-scene {
    position: absolute; left: 528px; top: 345px; width: 380px; height: 205px;
    border-radius: 10px;
    background: linear-gradient(100deg, #02060d 0%, #061327 30%, #0c2b52 60%, #1a4d86 85%, #10355f 100%);
    box-shadow: 0 0 24px rgba(2,85,163,.25);
  }
  .front-author {
    position: absolute; left: 500px; width: 420px; top: 620px;
    text-align: center; font-family: "Cinzel", serif; font-size: 22px; letter-spacing: 0.5px;
  }
</style>
</head>
<body>
  <main class="spread">
    <div class="sky" role="img" aria-label="Dark cloudy night sky scattered with stars"></div>
    <div class="spine"></div>

    <section class="back-cover">
      <h2 class="back-title">AMBER HOLLOWS</h2>
      <p class="back-subtitle">A Collection of Short Stories</p>
      <p class="back-author">DANA WHITCOMBE</p>
      <div class="author-photo" role="img" aria-label="Author portrait photo"></div>
      <div class="blurb blurb-side">
        <p>This fascinating collection of short stories is a unique blend of science fiction, action, and historical fiction that will entertain and challenge you.</p>
        <p>In Amber Hollows’ 11 intriguing stories, we experience one isolated man’s survival as he holds out and awaits the terrifying arrival of otherworldly visitors; firsthand battlefield accounts with some strange occurrences in both WW II and the Revolutionary War; and a tiger hunt in India that goes very wrong.</p>
      </div>
      <p class="blurb blurb-wide">We also see tales of modern woe revolving around some of life’s common miseries, accompanied by brave and unexpected measures to fight against them. In addition, we witness an awkward and dangerous stay in an underground bunker with an unstable host; two astronauts stranded on a lifeless asteroid who only have one old-fashioned form of entertainment; an eerie post-plague world dominated by an unlikely species; and an eccentric astronaut orbiting the Earth who is happiest on his own, except for one furry exception. Dana Whitcombe’s interesting stories travel in different directions, but spring from one deep source: the darker side of the imagination.</p>
    </section>

    <section class="spine-text">
      <p class="spine-title">AMBER HOLLOWS</p>
      <p class="spine-subtitle">A Collection of Short Stories</p>
      <p class="spine-author">DANA<br>WHITCOMBE</p>
    </section>

    <section class="front-cover">
      <div class="moon" role="img" aria-label="Full moon"></div>
      <h1 class="front-title">AMBER<br>HOLLOWS</h1>
      <p class="front-subtitle">A Collection of Short Stories</p>
      <div class="front-scene" role="img" aria-label="Silhouette of a man sitting on a hill in contemplation beside glowing blue starlit clouds"></div>
      <p class="front-author">DANA WHITCOMBE</p>
    </section>
  </main>
</body>
</html>
```